Wordpress Design Project (Bramblewick)

We need a wordpress design for an established auction and real estate company based in New Hampshire. The winning design will incorporate the colors of logo (red and blue) creatively with black or gray in a very professional and clean layout. Client mentions liking the site http://www.veltranbids.com/ as a general idea.

Industry/Entity Type

Real Estate

Requirements
Must have
• Navigation:
1) Home (lorem text)
2) Upcoming Auctions
3) Auction Results
4) Sell or Consign
5) About Us
6) Services
7) FAQ
8) Contact Us

Site will have slideshow, initial image attached.
Sidebar widgets:
- Email sign up form
- Featured Auction (like at http://www.dorvexsalehouse.com) - - - - Video Widget
- Testimonials widget

Footer will have smaller logo, contact info, and 2 association logos (attached)
-
Nice to have
• use of drop-down menu design for 'Services'
1) Appraisals
2) Consulting
Should not have
• please use no gavels in the design

```html
<!DOCTYPE html>
<html lang="en">
<head>
<meta charset="utf-8">
<title>Bramblewick Auctioneers</title>
<link href="https://fonts.googleapis.com/css2?family=Cabin:wght@400;500;600;700&family=Arimo:wght@400;700&display=swap" rel="stylesheet">
<style>
:root{
  --navy:#0d1a5c;
  --navy-dark:#0a1448;
  --red:#8c1124;
  --red-bright:#a8172e;
  --page:#f5f5f6;
  --line:#d6d6d8;
  --ink:#1c1c1c;
  --muted:#333;
  --footer:#1d1d1d;
  --footer-bar:#2b2b2b;
  --grey-btn:#2e2e2e;
}
*{box-sizing:border-box;margin:0;padding:0}
html,body{width:960px;height:1200px;overflow:hidden}
body{position:relative;background:var(--page);font-family:Arimo,Arial,sans-serif;color:var(--ink)}
.abs{position:absolute}

/* header */
.site-header{left:0;top:0;width:960px;height:106px;background:linear-gradient(#fbfbfb,#ececed)}
.brand{left:100px;top:24px;display:flex;align-items:center;gap:8px}
.brand-dot{width:58px;height:58px;border-radius:50%;background:var(--navy)}
.brand-name{font-family:Cabin,sans-serif;font-size:22px;color:var(--navy);letter-spacing:1px}
.phone{left:728px;top:28px;display:flex;align-items:center;gap:12px;font-family:Cabin,sans-serif;font-size:18px;color:var(--red)}
.connected{left:597px;top:75px;font-size:11.5px;color:#111}
.socials{left:698px;top:68px;display:flex;gap:8px}
.socials span{width:28px;height:28px;border-radius:5px;background:var(--navy)}
.socials span:nth-child(odd){background:var(--red)}

.band-top{left:0;top:106px;width:960px;height:7px;background:var(--red)}
.main-nav{left:0;top:113px;width:960px;height:35px;background:var(--navy);border-top:1px solid #2b3a86;border-bottom:2px solid #e9e9ee}
.main-nav ul{list-style:none;display:flex;position:absolute;left:82px;top:0;height:33px}
.main-nav li{font-family:Cabin,sans-serif;font-size:11.5px;color:#fff;line-height:33px;padding:0 18px;border-right:1px solid #25327a;position:relative}
.main-nav li:last-child{border-right:0}
.main-nav .active::after{content:"";position:absolute;left:50%;bottom:3px;margin-left:-3px;border:3px solid transparent;border-top:4px solid #fff}
.dropdown{left:536px;top:148px;width:126px;height:65px;background:var(--navy);border-radius:0 0 5px 5px;z-index:3;padding:9px 5px}
.dropdown div{font-family:Cabin,sans-serif;font-size:11.5px;color:#fff;height:21px;line-height:21px;padding-left:13px;margin-bottom:4px;border-radius:4px}
.dropdown .on{background:var(--red-bright)}

/* hero */
.hero{left:0;top:148px;width:960px;height:270px;background:var(--red)}
.slide{left:81px;top:163px;width:490px;height:239px;background:#fff;padding:5px}
.slide div{width:100%;height:100%;background:linear-gradient(135deg,#3a3430,#8f877a 40%,#cfc6b4 60%,#5b5246)}
.video{left:578px;top:163px;width:299px;height:239px;background:#fff;padding:10px 9px}
.video-screen{position:relative;width:100%;height:100%;background:radial-gradient(circle at 50% 40%,#e6e6e6,#b9b9b9)}
.play{position:absolute;left:107px;top:78px;width:67px;height:48px;background:#2a2a2a;border-radius:3px}
.faint-name{position:absolute;left:60px;top:146px;display:flex;align-items:center;gap:6px;font-family:Cabin,sans-serif;font-size:15px;color:rgba(60,60,110,.35)}
.faint-name i{width:40px;height:40px;border-radius:50%;background:rgba(60,60,110,.25)}
.controls{position:absolute;left:0;bottom:0;width:100%;height:20px;background:#0b0b0b;color:#cfc;font-size:8px;line-height:20px;padding:0 10px;display:flex;justify-content:space-between}

/* content */
.welcome{left:81px;top:436px;display:flex;align-items:center;gap:10px;font-family:Cabin,sans-serif;font-size:13.5px;color:var(--navy)}
.welcome i{width:30px;height:30px;border-radius:50%;background:var(--navy)}
.welcome b{font-weight:400;color:var(--red)}
.intro{left:81px;top:477px;width:525px;font-size:9.4px;line-height:14px;color:#222}
.intro p+p{margin-top:14px}
.section-title{left:81px;top:578px;font-family:Cabin,sans-serif;font-size:14.5px;color:var(--red)}
.section-title span{color:var(--navy)}

.card{left:81px;width:553px;height:216px;background:linear-gradient(#fff,#ececec);border:1px solid var(--line)}
.card-head{height:31px;background:var(--navy);color:#fff;font-family:Arimo,sans-serif;font-weight:700;font-size:11.5px;letter-spacing:.3px;line-height:31px;padding-left:13px}
.card .thumb{left:14px;top:49px;width:119px;height:80px;border:1px solid #4a6aa0;background:linear-gradient(#8fb0d8,#d9dee4 45%,#6f8e4e 75%,#3e6125)}
.card .title{left:150px;top:47px;width:380px;color:var(--red);font-weight:700;font-size:11.5px;line-height:14.5px}
.card .loc{left:151px;top:82px;font-size:10.8px;line-height:12.5px;color:#222}
.btn{left:14px;width:120px;height:29px;border-radius:5px;color:#fff;font-weight:700;font-size:13px;display:flex;align-items:center;gap:8px;padding-left:16px}
.btn svg{flex:none}
.btn-details{top:142px;background:var(--red-bright)}
.btn-photos{top:180px;background:var(--navy)}
.card .bid{left:153px;top:147px;font-size:10.8px;line-height:15px;color:#222}
.card .bid b{color:var(--red);font-size:9.8px}

/* sidebar */
.side-head{left:646px;width:231px;height:29px;background:var(--navy);color:#fff;font-family:Arimo,sans-serif;font-size:15px;line-height:31px;padding-left:17px;letter-spacing:.3px}
.featured{left:646px;top:471px;width:231px;height:229px;background:linear-gradient(#fff,#e9e9ea);border:1px solid var(--line);text-align:center;font-size:9.6px;line-height:14px;color:#222}
.featured .session{margin-top:14px;font-weight:700;color:#444;padding:0 16px}
.featured .house{width:134px;height:86px;margin:9px auto 0;border:1px solid #bbb;background:linear-gradient(#6d9bd6,#dbe6ee 45%,#c9c4bb 65%,#5b7d3a)}
.featured .meta{margin-top:16px}
.featured .meta span{color:var(--red)}
.signup{left:645px;top:709px;width:233px;height:174px;background:var(--red);border-radius:6px}
.signup h3{position:absolute;left:13px;top:14px;font-family:Georgia,serif;font-size:14.5px;color:#fff;letter-spacing:.3px}
.field{position:absolute;left:13px;width:196px;height:27px;background:#fff;border-radius:3px;font-size:9.8px;color:#333;line-height:27px;padding-left:7px}
.join{position:absolute;left:85px;top:130px;width:121px;height:29px;background:var(--grey-btn);border-radius:5px;color:#fff;font-weight:700;font-size:13px;display:flex;align-items:center;gap:9px;padding-left:9px}
.testi{left:646px;top:919px;width:232px;height:137px;background:#f3f3f4;border:1px solid var(--line)}
.testi q{position:absolute;left:24px;top:20px;width:175px;font-size:9.6px;line-height:12.2px;color:#333;quotes:none}
.testi .mark{position:absolute;font-family:Georgia,serif;font-size:14px;font-weight:700;color:#333}
.testi .who{position:absolute;left:97px;top:111px;font-weight:700;font-size:9.8px;color:var(--red)}

/* footer */
.site-footer{left:0;top:1067px;width:960px;height:105px;background:var(--footer)}
.foot-title{left:83px;top:1084px;font-family:Cabin,sans-serif;font-size:13px;color:#fff}
.foot-info{left:83px;top:1108px;font-family:Cabin,sans-serif;font-weight:700;font-size:9.8px;line-height:14px;color:#fff}
.badge-square{left:430px;top:1110px;width:42px;height:37px;background:#6b6b6b}
.badge-rect{left:500px;top:1112px;width:137px;height:32px;background:#e8e8e8}
.foot-brand{left:723px;top:1100px;display:flex;align-items:center;gap:6px;font-family:Cabin,sans-serif;font-size:15px;color:#e8e8e8}
.foot-brand i{width:44px;height:44px;border-radius:50%;background:#cfcfcf}
.copy{left:0;top:1172px;width:960px;height:28px;background:var(--footer-bar);color:#fff;font-size:9.8px;text-align:center;line-height:28px}
</style>
</head>
<body>

<header class="abs site-header">
  <div class="abs brand"><span class="brand-dot"></span><span class="brand-name">BRAMBLEWICK</span></div>
  <div class="abs phone">
    <svg width="10" height="22" viewBox="0 0 10 22"><path d="M8 1C3 2 1 6 1 11s2 9 7 10l1-4-3-1c-1-2-1-8 0-10l3-1z" fill="var(--red)"/></svg>
    212 555 0184
  </div>
  <div class="abs connected">Stay Connected</div>
  <div class="abs socials" aria-label="Social links"><span></span><span></span><span></span><span></span><span></span></div>
</header>

<div class="abs band-top"></div>
<nav class="abs main-nav">
  <ul>
    <li>Home</li><li>Upcoming Auctions</li><li>Auction Results</li><li>Sell or Consign</li>
    <li class="active" style="padding:0 26px">Services</li><li>About Us</li><li style="padding:0 22px">FAQ</li><li>Contact Us</li>
  </ul>
</nav>
<div class="abs dropdown"><div class="on">Appraisals</div><div>Consulting</div></div>

<section class="abs hero"></section>
<div class="abs slide"><div role="img" aria-label="Slideshow photo of collectible coins in a display case"></div></div>
<div class="abs video">
  <div class="video-screen">
    <div class="faint-name"><i></i>BRAMBLEWICK</div>
    <div class="play"><svg width="67" height="48" viewBox="0 0 67 48"><path d="M26 13l19 11-19 11z" fill="#fff"/></svg></div>
    <div class="controls"><span>▶ &nbsp;&nbsp;00:00</span><span>00:00 &nbsp;&nbsp;◂)|||| &nbsp;⤢</span></div>
  </div>
</div>

<h1 class="abs welcome"><i></i><span><b>WELCOME TO</b> BRAMBLEWICK</span></h1>
<div class="abs intro">
  <p><strong>Lorem Ipsum is simply dummy text of the printing and typesetting industry.</strong> Lorem Ipsum has been the industry's standard dummy text ever since the 1500s, when an unknown printer took a galley of type and scrambled it to make a type specimen book. It has survived not only five centuries,</p>
  <p>unchanged. It was popularised in the 1960s with the release of Letraset sheets containing Lorem Ipsum passages, and</p>
</div>
<h2 class="abs section-title">CURRENT &amp; UPCOMING <span>AUCTIONS</span></h2>

<article class="abs card" style="top:604px">
  <div class="card-head">MARSH HOLLOW CLINIC IN ASHBURY, NH</div>
  <div class="abs thumb" role="img" aria-label="Photo of a large two-storey house"></div>
  <div class="abs title">Harlow Pike Auctions, LLC GAL 5120 - Everything sold to the high bidder</div>
  <div class="abs loc">Location:<br>Location 1 - 418 Millbrook Rd<br>Location 2 - 52 Cedar Run # 4<br>Ashbury, NH 03601</div>
  <div class="abs btn btn-details"><svg width="20" height="20" viewBox="0 0 20 20"><rect x="1" y="1" width="18" height="18" rx="3" fill="#fff"/><circle cx="9" cy="9" r="4" fill="none" stroke="var(--red)" stroke-width="2"/><path d="M12 12l4 4" stroke="var(--red)" stroke-width="2"/></svg>DETAILS</div>
  <div class="abs btn btn-photos"><svg width="22" height="16" viewBox="0 0 22 16"><rect x="1" y="3" width="20" height="12" rx="2" fill="#fff"/><rect x="4" y="1" width="5" height="3" fill="#fff"/><circle cx="11" cy="9" r="3.5" fill="var(--navy)"/></svg>PHOTOS</div>
  <div class="abs bid"><b>Online Bidding Only</b><br>Began:&nbsp; Friday, May 24, 2013 at 10:06 AM EDT<br>Ends:&nbsp; Wednesday, June 05, 2013 at 10:00 AM EDT</div>
</article>

<article class="abs card" style="top:839px;height:217px">
  <div class="card-head" style="padding-left:16px">MARSH HOLLOW CLINIC IN ASHBURY, NH</div>
  <div class="abs thumb" style="left:18px;top:51px" role="img" aria-label="Photo of a large two-storey house"></div>
  <div class="abs title" style="left:154px;top:49px">Harlow Pike Auctions, LLC GAL 5120 - Everything sold to the high bidder</div>
  <div class="abs loc" style="left:155px;top:85px">Location:<br>Location 1 - 418 Millbrook Rd<br>Location 2 - 52 Cedar Run # 4<br>Ashbury, NH 03601</div>
  <div class="abs btn btn-details" style="left:17px;top:145px"><svg width="20" height="20" viewBox="0 0 20 20"><rect x="1" y="1" width="18" height="18" rx="3" fill="#fff"/><circle cx="9" cy="9" r="4" fill="none" stroke="var(--red)" stroke-width="2"/><path d="M12 12l4 4" stroke="var(--red)" stroke-width="2"/></svg>DETAILS</div>
  <div class="abs btn btn-photos" style="left:17px;top:181px"><svg width="22" height="16" viewBox="0 0 22 16"><rect x="1" y="3" width="20" height="12" rx="2" fill="#fff"/><rect x="4" y="1" width="5" height="3" fill="#fff"/><circle cx="11" cy="9" r="3.5" fill="var(--navy)"/></svg>PHOTOS</div>
  <div class="abs bid" style="left:156px;top:153px"><b>Online Bidding Only</b><br>Began:&nbsp; Friday, May 24, 2013 at 10:06 AM EDT<br>Ends:&nbsp; Wednesday, June 05, 2013 at 10:00 AM EDT</div>
</article>

<aside>
  <div class="abs side-head" style="top:442px">Featured Auctions</div>
  <div class="abs featured">
    <div class="session">Session 1 : Multi Estate &amp; Consignment Auction</div>
    <div class="house" role="img" aria-label="Photo of the featured estate house"></div>
    <div class="meta"><span>Start Date / Time</span> : wedneday,<br>Aprail 10,2013 at 2pm</div>
    <div class="meta" style="margin-top:9px"><span>Location</span> : 1187 Quarry Lane,<br>Dunmore, NH 03814</div>
  </div>

  <div class="abs signup">
    <h3>Sign up for Auction Alerts</h3>
    <div class="field" style="top:44px">Enter your Name</div>
    <div class="field" style="top:83px">Enter your emal address</div>
    <div class="join"><svg width="26" height="20" viewBox="0 0 26 20"><rect x="1" y="3" width="24" height="16" rx="2" fill="#ddd"/><path d="M1 4l12 9 12-9" fill="none" stroke="#777" stroke-width="1.5"/></svg>Join Now</div>
  </div>

  <div class="abs side-head" style="top:890px;height:29px;padding-left:13px">Clients Testimonials</div>
  <div class="abs testi">
    <span class="mark" style="left:9px;top:14px">“</span>
    <q>Lorem Ipsum is simply dummy text of the printing and typesetting industry. Lorem Ipsum is simply dummy text of the printing and typesetting industry. Lorem Ipsum is simply dummy text of the printing and typesetting industry.</q>
    <span class="mark" style="left:196px;top:88px">”</span>
    <span class="who">Mr Tobias Renfield</span>
  </div>
</aside>

<footer class="abs site-footer"></footer>
<div class="abs foot-title">CONTACT INFO</div>
<div class="abs foot-info">Bramblewick&nbsp; Auctioneers<br>74 Elm Court • Larkfield, NH 03290<br>P: 603-555-0147 • F: 603-555-0192<br>Email : info@bramblewick.com</div>
<div class="abs badge-square" role="img" aria-label="Association badge"></div>
<div class="abs badge-rect" role="img" aria-label="Association badge"></div>
<div class="abs foot-brand"><i></i>BRAMBLEWICK</div>
<div class="abs copy">Copyright (C) Bramblewick Auctioneers 2013 - 2014 .&nbsp; All Rights Reserved</div>

</body>
</html>
```